Brochure design - tamber floors

i need a brochure design for my flooring business which is in the same style/theme as the attached file. the images chosen from framebay should be focused on quality flooring and presented in a corporate and professional way. this design will be intended for printed brochures which i can hand to my clients as part of the sales process... I have a logo which should be included into the design (attached)
- This design should be ready for "Z" folded leaflet format - similar to the file attached
The design should present the images i attached in the brief
the design should follow the theme of the attached complete, sample brochure
the design needs to present the attached company logo in a clear and impressive way.
the design should allow for text boxes near each of the images

```html
<!DOCTYPE html>
<html lang="en">
<head>
<meta charset="UTF-8">
<title>Flooring brochure – Z-fold inside spread</title>
<link href="https://fonts.googleapis.com/css2?family=Montserrat:wght@300;400&display=swap" rel="stylesheet">
<style>
  :root {
    --backdrop: #6b6e71;
    --panel-grey: #3b3b3c;
    --card-black: #070707;
    --band-grey: #8a8b8d;
    --band-dark: #2e2e2f;
    --accent-cyan: #36a9c7;
    --card-teal: #022b3a;
    --heading-blue: #3fb6d8;
    --body-text: #e9e9e9;
    --wood-light: #d79a55;
    --wood-mid: #a9713d;
    --wood-pale: #b99a86;
    --floor-dark: #4a3a30;
  }
  * { box-sizing: border-box; margin: 0; padding: 0; }
  html, body { width: 1200px; height: 900px; overflow: hidden; }
  body {
    background: var(--backdrop);
    font-family: "Montserrat", sans-serif;
    position: relative;
  }
  .brochure {
    position: absolute; left: 60px; top: 100px;
    width: 1080px; height: 700px;
    display: flex;
    box-shadow: 0 10px 30px rgba(0,0,0,.35);
  }
  .panel { position: relative; width: 360px; height: 700px; overflow: hidden; background: var(--panel-grey); }
  .panel--accent { background: var(--accent-cyan); }
  .bands { position: absolute; inset: 0; width: 100%; height: 100%; }
  .card {
    position: absolute; background: var(--card-black);
    padding: 22px 22px 20px; display: flex; flex-direction: column;
  }
  .panel--accent .card { background: var(--card-teal); }
  .photo { width: 100%; flex: none; }
  .photo--wood { background: linear-gradient(135deg, var(--wood-light), var(--wood-mid)); }
  .photo--pale { background: linear-gradient(135deg, #e6e1da, var(--wood-pale)); }
  .photo--dark { background: linear-gradient(160deg, #d9d4cc 0%, var(--floor-dark) 70%); }
  .photo--roll { background: linear-gradient(135deg, #6a5444, #c9a57f 55%, #d9cdb8); }
  .card-title {
    font-weight: 300; color: var(--heading-blue);
    font-size: 19px; letter-spacing: .5px; margin: 14px 0 6px;
  }
  .card-title--top { margin-top: 0; }
  .card-text { font-size: 9.5px; line-height: 1.45; color: var(--body-text); }
</style>
</head>
<body>
<main class="brochure">
  <section class="panel panel--left">
    <svg class="bands" viewBox="0 0 360 700" aria-hidden="true">
      <path d="M360 40 C 250 120, 200 220, 130 330" stroke="var(--band-grey)" stroke-width="14" fill="none"/>
      <path d="M0 420 C 80 390, 170 380, 360 370" stroke="var(--band-grey)" stroke-width="12" fill="none"/>
      <path d="M60 0 L 90 700" stroke="var(--band-dark)" stroke-width="30" fill="none"/>
      <path d="M270 560 C 290 610, 300 650, 310 700" stroke="var(--band-grey)" stroke-width="14" fill="none"/>
    </svg>
    <article class="card" style="left:22px;top:28px;width:310px;height:310px;">
      <div class="photo photo--wood" style="height:170px;" role="img" aria-label="Hands marking oak floor planks with a pencil"></div>
      <h2 class="card-title">Ceariosam volum</h2>
      <p class="card-text">As niam nimaximostia venihitat. Harchictis intiore hentotate venet estem harunt dignis nobit aute libus nonsequis si voluptatia cuptae et aut essum nihic tem.</p>
    </article>
    <article class="card" style="left:22px;top:360px;width:316px;height:318px;">
      <div class="photo photo--roll" style="height:170px;" role="img" aria-label="Installer kneeling and laying a roll of wood-effect vinyl flooring"></div>
      <h2 class="card-title">Ceariosam volum</h2>
      <p class="card-text">As niam nimaximostia venihitat. Harchictis intiore hentotate venet estem harunt dignis nobit aute libus nonsequis si voluptatia cuptae et aut essum nihic tem. Um voluptu rersped quunt quam nullitiat doluptat.</p>
    </article>
  </section>

  <section class="panel panel--middle">
    <svg class="bands" viewBox="0 0 360 700" aria-hidden="true">
      <path d="M0 40 C 60 20, 120 10, 200 0" stroke="var(--band-grey)" stroke-width="12" fill="none"/>
      <path d="M0 370 C 120 360, 240 350, 360 340" stroke="var(--band-grey)" stroke-width="12" fill="none"/>
    </svg>
    <article class="card" style="left:28px;top:20px;width:306px;height:174px;">
      <h2 class="card-title card-title--top">Ceariosam volum</h2>
      <p class="card-text">As niam nimaximostia venihitat. Harchictis intiore hentotate venet estem harunt dignis nobit aute libus nonsequis si voluptatia cuptae et aut essum nihic tem. Go etidet C. Vocupic ientetu ntelum oc, nium et inat atis constam intem aucompotium, untiam consimilus senihinem pro ne ine nocis consum note cuperdis supiori.</p>
    </article>
    <article class="card" style="left:28px;top:212px;width:306px;height:282px;">
      <div class="photo photo--wood" style="height:150px;" role="img" aria-label="Hand sanding the edge of a wooden stair tread"></div>
      <h2 class="card-title">Ceariosam volum</h2>
      <p class="card-text">As niam nimaximostia venihitat. Harchictis intiore hentotate venet estem harunt dignis nobit aute libus nonsequis si voluptatia cuptae et aut essum nihic tem.</p>
    </article>
    <article class="card" style="left:28px;top:512px;width:306px;height:168px;">
      <div class="photo photo--dark" style="height:126px;" role="img" aria-label="Worker applying finish to a dark glossy wooden floor"></div>
    </article>
  </section>

  <section class="panel panel--accent">
    <article class="card" style="left:24px;top:26px;width:310px;height:300px;">
      <div class="photo photo--dark" style="height:180px;" role="img" aria-label="Worker operating a floor sander on a wooden floor"></div>
      <h2 class="card-title">Ceariosam volum</h2>
      <p class="card-text">As niam nimaximostia venihitat. Harchictis intiore hentotate venet estem harunt dignis nobit aute libus nonsequis si voluptatia cuptae et aut essum nihic tem.</p>
    </article>
    <article class="card" style="left:24px;top:352px;width:310px;height:326px;">
      <div class="photo photo--pale" style="height:180px;" role="img" aria-label="Drum sander on a herringbone parquet floor"></div>
      <h2 class="card-title">Ceariosam volum</h2>
      <p class="card-text">As niam nimaximostia venihitat. Harchictis intiore hentotate venet estem harunt dignis nobit aute libus nonsequis si voluptatia cuptae et aut essum nihic tem. Um voluptu rersped quunt quam nullitiat doluptat.</p>
    </article>
  </section>
</main>
</body>
</html>
```